Bref créative |
Jewelry and Home ware website | ||
Studio Kelvara | ||
Jewelry | ||
www.studiokelvara.example | ||
Studio Kelvara is a new company which is just about to launch to the public. Studio Kelvara is a line of handmade jewelry and home ware made with semi precious materials. All pieces are designed and made by me (kela) Rosalind Theda Quarrington. At the moment the brand is very small and the website will be primary used as an online catalogue, eventually hoping to start online buying. | ||
Clean and simple designs, nothing to distract from pieces. |
Clean/Simple Conservative Elegant Traditional Feminine |
Browns | ||
Beiges /Off Whites | ||
Natural tones | ||
left side | ||
View logo on company url. | ||

```html
<!DOCTYPE html>
<html lang="en">
<head>
<meta charset="utf-8">
<title>Studio Kelvara — Handmade Jewelry &amp; Home Ware</title>
<link href="https://fonts.googleapis.com/css2?family=Pinyon+Script&family=Arimo:wght@400;700&display=swap" rel="stylesheet">
<style>
  :root {
    --cream: #f7f2e4;
    --cream-deep: #efe6cf;
    --brown-dark: #3f3029;
    --brown: #5a463a;
    --tan: #d8c08c;
    --tan-light: #e6d3a6;
    --panel: #f4f4f2;
    --panel-edge: #ffffff;
    --text: #4a3b32;
    --muted: #6d6158;
    --rule: #cfc3aa;
  }
  html, body {
    margin: 0;
    width: 1200px;
    height: 890px;
    overflow: hidden;
    background: var(--cream);
    font-family: "Arimo", Arial, sans-serif;
    color: var(--text);
  }
  .page {
    position: relative;
    width: 1200px;
    height: 890px;
    background:
      radial-gradient(ellipse 520px 380px at 120px 380px, rgba(225,210,175,0.35), transparent 70%),
      radial-gradient(ellipse 480px 360px at 1080px 140px, rgba(225,210,175,0.35), transparent 70%),
      var(--cream);
  }
  .script { font-family: "Pinyon Script", cursive; }

  .brand { position: absolute; left: 0; width: 1200px; top: 26px; text-align: center; color: var(--brown-dark); }
  .brand-name { font-family: "Pinyon Script", cursive; font-size: 62px; line-height: 1; }
  .brand-owner { font-family: "Pinyon Script", cursive; font-size: 17px; margin-top: 8px; }

  .nav { position: absolute; left: 200px; top: 144px; width: 798px; height: 48px; display: flex; }
  .nav a {
    display: flex; align-items: center; justify-content: center;
    height: 48px; background: var(--tan); color: var(--brown-dark);
    font-size: 15px; text-decoration: none; border-right: 1px solid #c4a972;
    border-radius: 4px 4px 0 0;
  }
  .nav a.active { background: var(--brown-dark); color: #fff; }
  .nav .search {
    flex: 1; background: var(--brown-dark); border-radius: 4px 4px 0 0;
    display: flex; align-items: center; padding: 0 14px;
  }
  .search-box {
    flex: 1; height: 24px; background: #fff; border-radius: 3px;
    display: flex; align-items: center; justify-content: space-between;
    padding: 0 8px; font-size: 13px; color: #555;
  }

  .hero {
    position: absolute; left: 192px; top: 190px; width: 813px; height: 308px;
    background: linear-gradient(180deg, #f8f8f7, #ececea);
    border: 6px solid var(--panel-edge); box-sizing: border-box;
    box-shadow: 0 4px 14px rgba(80,60,40,0.25);
  }
  .hero-necklace {
    position: absolute; left: 30px; top: 20px; width: 250px; height: 240px;
    background: radial-gradient(ellipse at 50% 55%, #d9c28c 0%, #2f5a4a 45%, transparent 70%);
  }
  .hero-title {
    position: absolute; left: 290px; top: 90px; font-size: 46px; line-height: 1.2;
    color: var(--brown-dark); text-align: center;
  }
  .hero-model {
    position: absolute; right: 8px; top: 8px; width: 170px; height: 280px;
    background: linear-gradient(180deg, #d6b8a0, #f1ece6 60%, #fafafa);
  }
  .dots { position: absolute; left: 18px; bottom: 10px; display: flex; gap: 4px; }
  .dots span { width: 9px; height: 9px; border-radius: 50%; background: var(--tan); }
  .dots span:first-child { background: var(--brown-dark); }

  .feature {
    position: absolute; top: 524px; height: 126px;
    background: linear-gradient(180deg, #f4f4f3, #e3e3e1);
    border: 5px solid #fff; box-sizing: border-box;
    box-shadow: 0 2px 8px rgba(80,60,40,0.2);
  }
  .feature-photo { position: absolute; left: 6px; top: 6px; bottom: 6px; width: 110px; }
  .feature-label {
    position: absolute; right: 16px; top: 0; bottom: 0; display: flex; align-items: center;
    font-family: "Pinyon Script", cursive; font-size: 32px; line-height: 1.05; text-align: center;
    color: var(--brown-dark);
  }

  .about { position: absolute; left: 192px; top: 668px; width: 540px; }
  .about h2 { font-family: "Pinyon Script", cursive; font-weight: 400; font-size: 28px; margin: 0; color: var(--brown-dark); }
  .about p { font-size: 11.5px; line-height: 15px; margin: 6px 0 0; color: var(--muted); }
  .read-more { font-family: "Pinyon Script", cursive; font-size: 22px; margin-top: 10px; color: var(--brown-dark); }

  .shop {
    position: absolute; left: 760px; top: 680px; width: 245px; height: 114px;
    background: #fff; border: 1px solid #e4dccb; box-sizing: border-box;
  }
  .shop-title { position: absolute; left: 12px; top: 14px; font-family: "Pinyon Script", cursive; font-size: 24px; color: var(--brown-dark); }
  .shop-text { position: absolute; left: 12px; top: 50px; width: 120px; font-size: 11px; font-weight: 700; line-height: 13px; color: var(--text); }
  .shop-photo { position: absolute; right: 6px; top: 6px; width: 108px; height: 100px; background: linear-gradient(180deg, #e7e1d6, #cbbfae); }

  .footer-rule { position: absolute; left: 192px; top: 825px; width: 813px; height: 1px; background: var(--rule); }
  .footer-links { position: absolute; left: 192px; top: 840px; font-size: 12px; color: var(--brown-dark); }
  .footer-links span { margin: 0 6px; color: var(--muted); }
  .copyright { position: absolute; left: 192px; top: 862px; font-size: 11px; color: var(--brown-dark); }
  .social { position: absolute; left: 944px; top: 838px; display: flex; gap: 8px; }
  .social span { width: 28px; height: 28px; border-radius: 50%; background: var(--brown-dark); }
</style>
</head>
<body>
<div class="page">
  <header class="brand">
    <div class="brand-name">Studio Kelvara</div>
    <div class="brand-owner">Rosalind Theda Quarrington</div>
  </header>

  <nav class="nav">
    <a class="active" style="width:96px" href="#">Home</a>
    <a style="width:101px" href="#">About Us</a>
    <a style="width:96px" href="#">Jewelry</a>
    <a style="width:144px" href="#">Home Wmade</a>
    <a style="width:92px" href="#">Contact Us</a>
    <div class="search">
      <div class="search-box">Search
        <svg width="14" height="14" viewBox="0 0 14 14"><circle cx="5.5" cy="5.5" r="4" fill="none" stroke="#555" stroke-width="1.6"/><line x1="8.5" y1="8.5" x2="13" y2="13" stroke="#555" stroke-width="1.8"/></svg>
      </div>
    </div>
  </nav>

  <section class="hero">
    <div class="hero-necklace" role="img" aria-label="Gold and green stone collar necklace on leather cord"></div>
    <div class="hero-title script">Lorem ipsum d<br>sit amet, cons.</div>
    <div class="hero-model" role="img" aria-label="Model in white dress wearing the collar necklace"></div>
    <div class="dots"><span></span><span></span><span></span><span></span></div>
  </section>

  <a class="feature" style="left:192px;width:253px" href="#">
    <div class="feature-photo" role="img" aria-label="Gold and green collar necklace detail" style="background:linear-gradient(135deg,#d8c08c,#3d6555)"></div>
    <div class="feature-label">Jewelry</div>
  </a>
  <a class="feature" style="left:474px;width:250px" href="#">
    <div class="feature-photo" role="img" aria-label="Handmade wooden and pearl spoons" style="background:linear-gradient(135deg,#5a3a28,#e8e4dc)"></div>
    <div class="feature-label">Home<br>Wmade</div>
  </a>
  <a class="feature" style="left:755px;width:250px" href="#">
    <div class="feature-photo" role="img" aria-label="Carved wooden cuff bracelet" style="background:linear-gradient(135deg,#8a4a28,#c98a5a)"></div>
    <div class="feature-label">Latest<br>Products</div>
  </a>

  <section class="about">
    <h2>Meet Rosalind Theda Quarrington (kela)</h2>
    <p>Lorem ipsum dolor sit amet, consectetur adipisicing elit, sed do eiusmod tempor incididunt ut labore et dolore magna aliqua. Ut enim ad minim veniam, quis nostrud exercitation ullamco laboris nisi ut aliquip ex ea commodo consequat. Duis aute irure dolor in reprehenderit in voluptate velit esse cillum dolore eu fugiat nulla pariatur. Excepteur sint occa aliqua. Ut enim ad minim veniam, quis nostrud exercitation ullamco.</p>
    <div class="read-more">Read More...</div>
  </section>

  <aside class="shop">
    <div class="shop-title">Online Shop</div>
    <div class="shop-text">Lorem ipsum dolor sit sa d tempor incididun. tetur adipiscing elit.</div>
    <div class="shop-photo" role="img" aria-label="Pendant necklaces hanging on a display"></div>
  </aside>

  <div class="footer-rule"></div>
  <div class="footer-links">Home<span>|</span>About Us<span>|</span>Jewelry<span>|</span>Home wmade<span>|</span>Contact Us</div>
  <div class="copyright">Copyright 2013</div>
  <div class="social" aria-label="Social links"><span></span><span></span></div>
</div>
</body>
</html>
```